Figure for a research paper

I am working on designing a figure for a research paper that illustrates the effect of KADO Pathways assessment on student outcomes over time by impacting teacher bias and teacher perception of student growth. I built the attached figure via powerpoint. It includes the very basic elements but it does not look great and I am not sure that it is clearly depicting what I am hoping to illustrate. I would like for you to build an illustration of this idea that i can include in the paper.

```html
<!DOCTYPE html>
<html lang="en">
<head>
<meta charset="utf-8">
<title>Effectiveness of SEL Program on the Student</title>
<link rel="stylesheet" href="https://fonts.googleapis.com/css2?family=Arimo:wght@700&display=swap">
<style>
  :root {
    --paper: #ffffff;
    --navy: #1b6183;
    --signal-red: #e8202a;
    --label-white: #ffffff;
    --soft-shadow: rgba(0, 0, 0, 0.28);
  }
  html, body {
    margin: 0;
    padding: 0;
    width: 1200px;
    height: 1000px;
    overflow: hidden;
    background: var(--paper);
  }
  .figure {
    display: block;
    width: 1200px;
    height: 1000px;
    font-family: "Arimo", "Helvetica Neue", Arial, sans-serif;
    font-weight: 700;
  }
  .chart-title { fill: var(--navy); font-size: 39px; }
  .axis-label { fill: var(--navy); font-size: 28px; }
  .annotation { fill: var(--signal-red); font-size: 27px; }
  .assessment-label { fill: var(--label-white); font-size: 27px; }
  .axis-line { stroke: var(--navy); stroke-width: 8; fill: none; }
  .axis-head { fill: var(--navy); }
  .outcome-area { fill: var(--navy); }
  .perception-curve {
    fill: none;
    stroke: var(--signal-red);
    stroke-width: 10;
    stroke-linecap: round;
    stroke-dasharray: 0 19;
  }
  .pointer-red { fill: var(--signal-red); }
  .pointer-white { fill: var(--label-white); }
</style>
</head>
<body>
<svg class="figure" viewBox="0 0 1200 1000" xmlns="http://www.w3.org/2000/svg" role="img"
     aria-label="Chart: effectiveness of an SEL program on the student over time, comparing teacher perception with KADO Pathways assessment">
  <defs>
    <filter id="soft-shadow" x="-10%" y="-10%" width="120%" height="130%">
      <feDropShadow dx="0" dy="4" stdDeviation="6" flood-color="var(--soft-shadow)" flood-opacity="0.35"/>
    </filter>
  </defs>

  <text class="chart-title" x="598" y="212" text-anchor="middle" filter="url(#soft-shadow)">Effectiveness of SEL Program on the Student</text>

  <g class="axes" filter="url(#soft-shadow)">
    <line class="axis-line" x1="133" y1="245" x2="133" y2="752"/>
    <polygon class="axis-head" points="120,248 146,248 133,228"/>
  </g>

  <path class="outcome-area" filter="url(#soft-shadow)"
        d="M128 742 L140 742 C450 680, 800 560, 1068 322 L1068 752 L128 752 Z"/>

  <path class="perception-curve" d="M145 735 C450 658, 800 520, 1058 288"/>

  <g class="bias-callout">
    <text class="annotation" x="400" y="522" text-anchor="middle">Teacher Bias</text>
    <rect class="pointer-red" x="393" y="536" width="14" height="50"/>
    <polygon class="pointer-red" points="386,584 414,584 400,606"/>
  </g>

  <g class="perception-callout">
    <text class="annotation" text-anchor="middle">
      <tspan x="790" y="298">Teacher’s inaccurate</tspan>
      <tspan x="790" y="326">perception of student</tspan>
      <tspan x="790" y="354">growth or learning</tspan>
    </text>
    <rect class="pointer-red" x="783" y="368" width="14" height="48"/>
    <polygon class="pointer-red" points="776,414 804,414 790,437"/>
  </g>

  <g class="assessment-callout">
    <polygon class="pointer-white" points="906,486 934,486 920,464"/>
    <rect class="pointer-white" x="913" y="485" width="14" height="50"/>
    <text class="assessment-label" text-anchor="middle">
      <tspan x="915" y="568">KADO Pathways</tspan>
      <tspan x="915" y="597">Assessment</tspan>
    </text>
  </g>

  <text class="axis-label" x="601" y="801" text-anchor="middle">Time</text>
</svg>
</body>
</html>
```